Mission Statement Board for front lobby

We need a mission statement board for our front lobby at our company called PatternForge. We are a web content management company that builds websites for our clients. We would like two boards, same size, canvas material (not thin poster board or anything like that) size H 3' x L 2', white background, blue and black colored font, our logo on top in blue/gray/black and some blue coloring around top and bottom, kind of framing the white background. Please reference our very rough draft we did in Word so you get an idea of what we're thinking- the attachment shows what we would like on each board. Reference our website to see logo and fonts if you would like, please keep the board similar to our fonts and colors. www.patternforge-example.com

Contact info: Donna Whitlock
Email: donna.whitlock@patternforge-example.com
Phone: 555-217-4039
Updates

Please do not include in a design my contact info, no email donna.whitlock@patternforge-example.com, no phone # 555-217-4039. I added that info to the project when I posted it, but it is not part of the design.... reference attachment posted in project with exactly what we want.

Target Market(s)

Clients & employees in the office who will see the boards in lobby

Industry/Entity Type

It Company

Font styles to use
Other font styles liked:
• reference attachment (but font is flexible within reason)

Colors
33a6d7
0255a3
eaf1f7
0292cd
85cae6
cee9f5
000000
5c5c5c
959595

Requirements
Must have
• Needs to be a professional sign that hangs on wall, company logo, cohesive colors and fonts
Nice to have
• Get creative with the border/framing around the white background
Should not have
• Unprofessional fonts, typos, thin cheap looking poster board materal.

```html
<!DOCTYPE html>
<html lang="en">
<head>
<meta charset="UTF-8">
<title>PatternForge Mission Statement Board</title>
<link href="https://fonts.googleapis.com/css2?family=Lato:wght@400;700&display=swap" rel="stylesheet">
<style>
  :root {
    --backdrop: #2e3b45;
    --deep-blue: #0255a3;
    --bright-blue: #0292cd;
    --sky-blue: #33a6d7;
    --pale-blue: #85cae6;
    --mist-blue: #cee9f5;
    --ice: #eaf1f7;
    --ink: #000000;
    --steel: #5c5c5c;
    --silver: #959595;
    --paper: #ffffff;
  }
  * { margin: 0; padding: 0; box-sizing: border-box; }
  html, body {
    width: 1200px;
    height: 900px;
    overflow: hidden;
    background: var(--backdrop);
    font-family: "Lato", sans-serif;
  }
  .board {
    position: absolute;
    left: 320px;
    top: 30px;
    width: 560px;
    height: 840px;
    background: var(--paper);
    overflow: hidden;
    box-shadow: 0 14px 40px rgba(0,0,0,0.45);
  }
  .board-frame {
    position: absolute;
    inset: 0;
    width: 100%;
    height: 100%;
  }
  .brand {
    position: absolute;
    top: 205px;
    right: 42px;
    display: flex;
    align-items: center;
    gap: 10px;
  }
  .brand-dot {
    width: 18px;
    height: 18px;
    border-radius: 50%;
    background: var(--sky-blue);
  }
  .brand-name {
    font-weight: 700;
    font-size: 26px;
    color: var(--steel);
    letter-spacing: 0.5px;
  }
  .statement {
    position: absolute;
    left: 62px;
    right: 44px;
  }
  .statement-mission { top: 318px; }
  .statement-faith { top: 482px; }
  .statement-title {
    font-weight: 400;
    font-size: 29px;
    color: var(--bright-blue);
    line-height: 1.15;
  }
  .statement-body {
    font-weight: 400;
    font-size: 25px;
    line-height: 1.36;
    color: var(--ink);
    text-align: justify;
    text-align-last: left;
    hyphens: manual;
  }
</style>
</head>
<body>
  <main class="board">
    <svg class="board-frame" viewBox="0 0 560 840" aria-hidden="true">
      <defs>
        <linearGradient id="top-blue" x1="0" y1="0" x2="1" y2="0">
          <stop offset="0" stop-color="#1f47b0"/>
          <stop offset="0.6" stop-color="#1f63d6"/>
          <stop offset="1" stop-color="#2f8cf0"/>
        </linearGradient>
        <linearGradient id="silver-sweep" x1="0" y1="0" x2="1" y2="0">
          <stop offset="0" stop-color="#8d9499"/>
          <stop offset="0.35" stop-color="#f4f6f7"/>
          <stop offset="0.6" stop-color="#a3aab0"/>
          <stop offset="1" stop-color="#ffffff"/>
        </linearGradient>
        <linearGradient id="cyan-swoosh" x1="0" y1="0" x2="1" y2="0.5">
          <stop offset="0" stop-color="#5fe3f5"/>
          <stop offset="0.45" stop-color="#cee9f5"/>
          <stop offset="1" stop-color="#ffffff" stop-opacity="0"/>
        </linearGradient>
        <linearGradient id="bottom-blue" x1="0" y1="0" x2="1" y2="0">
          <stop offset="0" stop-color="#1e3fa6"/>
          <stop offset="1" stop-color="#2a6fe0"/>
        </linearGradient>
      </defs>

      <path class="frame-swoosh" d="M0 290 C120 215 300 190 560 178 L560 190 C330 205 150 250 0 470 Z" fill="url(#cyan-swoosh)"/>
      <path class="frame-swoosh-edge" d="M0 300 C110 240 280 210 560 190" fill="none" stroke="#9fe9f7" stroke-width="6" opacity="0.7"/>

      <path class="frame-top" d="M0 0 H560 V155 C400 140 180 170 0 248 Z" fill="url(#top-blue)"/>
      <path class="frame-top-silver" d="M0 248 C180 170 400 140 560 155 L560 168 C400 156 190 184 0 268 Z" fill="url(#silver-sweep)"/>

      <path class="frame-bottom-silver" d="M0 790 C220 790 420 760 560 668 L560 690 C420 770 220 802 0 806 Z" fill="url(#silver-sweep)"/>
      <path class="frame-bottom" d="M0 806 C220 802 420 770 560 690 V840 H0 Z" fill="url(#bottom-blue)"/>
      <path class="frame-bottom-glow" d="M0 812 C230 808 430 778 560 705" fill="none" stroke="#eaf1f7" stroke-width="3" opacity="0.6"/>
    </svg>

    <div class="brand">
      <span class="brand-dot"></span>
      <span class="brand-name">PatternForge</span>
    </div>

    <section class="statement statement-mission">
      <h2 class="statement-title">Our Mission Statement:</h2>
      <p class="statement-body">We design and implement extraor-dinary web solutions to help our clients achieve their goals.</p>
    </section>

    <section class="statement statement-faith">
      <h2 class="statement-title">Our Faith...</h2>
      <p class="statement-body">We reflect the love of Christ in us and through us to our fellow employees, partners and clients.</p>
    </section>
  </main>
</body>
</html>
```